Templates for Construction Company

We are looking to have templates prepared for all aspects of our letter sending. Using our brand design. with similar layouts that look the same.

Letterheads design & Email signatures

We use letter heads for - quotes, contract correspondence, variations, formal letters, invitations

Target Market(s)

Clients documents sent in emails

Industry/Entity Type

Construction

Font styles to use
Serif
Sans Serif

Colors
0054AA
0677BA
7BADD7
CADEEF
E8F1F8

Requirements
Must have
• Easy to read, water marks on page
Nice to have
• Different options for different letters

```html
<!DOCTYPE html>
<html lang="en">
<head>
<meta charset="utf-8">
<title>Forge Construction Group — Stationery Templates</title>
<link href="https://fonts.googleapis.com/css2?family=Poppins:wght@400;500;600&display=swap" rel="stylesheet">
<style>
  :root {
    --brand-blue: #5b87c7;
    --brand-grey: #666666;
    --tagline-grey: #555555;
    --frame-grey: #8a8a8a;
    --label-grey: #555555;
    --ink: #1d1d1d;
    --watermark: #dfe7f3;
    --paper: #ffffff;
  }
  * { margin: 0; padding: 0; box-sizing: border-box; }
  html, body { width: 1200px; height: 848px; overflow: hidden; background: var(--paper); }
  body { font-family: "Poppins", sans-serif; color: var(--ink); }
  .canvas { position: relative; width: 1200px; height: 848px; }

  .sheet { position: absolute; border: 1.5px solid var(--frame-grey); background: var(--paper); overflow: hidden; }
  .letterhead { left: 65px; top: 95px; width: 465px; height: 655px; }
  .envelope { left: 642px; top: 95px; width: 518px; height: 280px; }

  .piece-label { position: absolute; font-size: 16px; color: var(--label-grey); line-height: 1; white-space: nowrap; }
  .label-letterhead { left: 65px; top: 777px; }
  .label-envelope { left: 1091px; top: 388px; }
  .label-signature { left: 630px; top: 466px; }

  .wordmark { position: absolute; font-weight: 600; white-space: nowrap; }
  .wordmark .name { display: block; color: var(--brand-blue); line-height: 1.4; }
  .wordmark .tagline { display: block; color: var(--tagline-grey); font-weight: 500; line-height: 1; letter-spacing: 0.02em; }

  .letterhead .wordmark { left: 16px; top: 20px; }
  .letterhead .wordmark .name { font-size: 40px; }
  .letterhead .wordmark .tagline { font-size: 7.5px; }

  .envelope .wordmark { left: 22px; top: 32px; }
  .envelope .wordmark .name { font-size: 40px; }
  .envelope .wordmark .tagline { font-size: 7.5px; }

  .side-bands { position: absolute; display: flex; gap: 3px; bottom: 0; }
  .side-bands span { width: 5.5px; height: 100%; background: var(--brand-grey); }
  .side-bands span.accent { background: var(--brand-blue); }
  .letterhead .side-bands { left: 15px; top: 90px; }
  .envelope .side-bands { left: 22px; top: 102px; }

  .watermark { position: absolute; left: 120px; top: 258px; font-weight: 600; white-space: nowrap; }
  .watermark .name { display: block; font-size: 90px; line-height: 1.4; color: var(--watermark); }
  .watermark .tagline { display: block; font-size: 16px; line-height: 1; letter-spacing: 0.03em; color: var(--watermark); }

  .letter-footer { position: absolute; left: 0; top: 618px; width: 100%; height: 30px; font-size: 9.5px; line-height: 11px; color: var(--ink); white-space: nowrap; }
  .letter-footer .col { position: absolute; top: 0; }
  .letter-footer .col-address { left: 52px; }
  .letter-footer .col-web { left: 238px; }
  .letter-footer .col-phone { left: 371px; }
  .letter-footer .divider { position: absolute; top: -4px; width: 1.5px; height: 30px; background: var(--ink); }
  .letter-footer .divider-one { left: 224px; }
  .letter-footer .divider-two { left: 357px; }

  .signature { position: absolute; left: 634px; top: 528px; width: 540px; height: 192px; }
  .signature .wordmark { left: 0; top: 50px; }
  .signature .wordmark .name { font-size: 62px; }
  .signature .wordmark .tagline { font-size: 11.5px; }
  .signature .rule { position: absolute; left: 205px; top: 0; width: 1.5px; height: 192px; background: var(--ink); }
  .signature .details { position: absolute; left: 238px; top: 0; color: var(--label-grey); font-size: 16px; line-height: 18px; white-space: nowrap; }
  .person-name { font-size: 29px; line-height: 32px; color: var(--brand-blue); font-weight: 400; }
  .person-name strong { font-weight: 600; }
  .contact-lines { margin-top: 12px; }
  .contact-lines .gap { display: inline-block; width: 18px; }
  .address-lines { margin-top: 17px; }
  .social-row { display: flex; gap: 16px; margin-top: 12px; }
  .social-row span { width: 29px; height: 29px; border-radius: 50%; background: var(--brand-blue); }
</style>
</head>
<body>
<main class="canvas">

  <section class="sheet letterhead" aria-label="Letterhead A4">
    <div class="wordmark"><span class="name">Forge</span><span class="tagline">CONSTRUCTION GROUP</span></div>
    <div class="side-bands"><span></span><span class="accent"></span><span></span></div>
    <div class="watermark" aria-hidden="true"><span class="name">Forge</span><span class="tagline">CONSTRUCTION GROUP</span></div>
    <footer class="letter-footer">
      <div class="col col-address">8888 Address Street,&nbsp; San Address<br>United States of America</div>
      <div class="divider divider-one"></div>
      <div class="col col-web">wwwforgebuild.com<br>forgeinquire.gmail.com</div>
      <div class="divider divider-two"></div>
      <div class="col col-phone">1234-888-8888<br>1234-000-9999</div>
    </footer>
  </section>
  <p class="piece-label label-letterhead">Letterhead A4 size</p>

  <section class="sheet envelope" aria-label="Envelope">
    <div class="wordmark"><span class="name">Forge</span><span class="tagline">CONSTRUCTION GROUP</span></div>
    <div class="side-bands"><span></span><span class="accent"></span><span></span></div>
  </section>
  <p class="piece-label label-envelope">Envelope</p>

  <p class="piece-label label-signature">Email Signature</p>
  <section class="signature" aria-label="Email signature">
    <div class="wordmark"><span class="name">Forge</span><span class="tagline">CONSTRUCTION GROUP</span></div>
    <div class="rule"></div>
    <div class="details">
      <p class="person-name">John <strong>Doe</strong></p>
      <p class="person-role">Sales &amp; Marketing Director</p>
      <p class="contact-lines">M: +67 75 00 00 008<br>P:&nbsp; 1234-888-8888<span class="gap"></span>1234-000-9999</p>
      <p class="address-lines">8888 Address Street,&nbsp; San Address<br>United States of America</p>
      <div class="social-row" role="img" aria-label="Social media profile links">
        <span></span><span></span><span></span><span></span><span></span>
      </div>
    </div>
  </section>

</main>
</body>
</html>
```